Business Card Design Project

We would need a business name card for our online website business, http://www.plimo.com.sg/. We would need to include our website on the name card as well.

Target Market(s)

Adults and kids in Singapore, mainly expatriates

Industry/Entity Type

Business

Font styles to use
Sans Serif

Colors

Designer to choose colors to be used in the design.

Requirements
Must have
• Must include our "plimo" logo and we would like our name card to be printed on light craft paper material

```html
<!DOCTYPE html>
<html lang="en">
<head>
<meta charset="utf-8">
<title>plimo – business card</title>
<link href="https://fonts.googleapis.com/css2?family=Arimo:wght@400;700&family=Sniglet:wght@400;800&display=swap" rel="stylesheet">
<style>
  :root {
    --backdrop: #5f5f5f;
    --kraft: #ebe2cb;
    --kraft-light: #f3ecda;
    --ink: #141414;
    --mark-navy: #26387f;
    --sweets: #f0642a;
    --chocolates: #27b5c9;
    --drinks: #fdd22a;
    --snacks: #f49ac8;
    --badge-text: #ffffff;
  }
  * { margin: 0; padding: 0; box-sizing: border-box; }
  html, body {
    width: 1200px;
    height: 900px;
    overflow: hidden;
  }
  body {
    background: var(--backdrop);
    font-family: "Arimo", Arial, sans-serif;
    position: relative;
  }
  .card {
    position: absolute;
    left: 300px;
    width: 600px;
    height: 343px;
    background: linear-gradient(135deg, var(--kraft) 0%, var(--kraft-light) 100%);
    border-radius: 3px;
    box-shadow: 0 6px 18px rgba(0, 0, 0, 0.35);
  }
  .card--front { top: 90px; }
  .card--back { top: 467px; }

  .brand {
    position: absolute;
    top: 46px;
    left: 0;
    right: 0;
    display: flex;
    justify-content: center;
    align-items: center;
    gap: 26px;
  }
  .brand__dot {
    width: 96px;
    height: 96px;
    border-radius: 50%;
    background: var(--mark-navy);
  }
  .brand__name {
    font-family: "Arimo", Arial, sans-serif;
    font-weight: 400;
    font-size: 56px;
    letter-spacing: 2px;
    color: var(--ink);
    text-transform: uppercase;
  }

  .categories {
    position: absolute;
    bottom: 44px;
    left: 0;
    right: 0;
    display: flex;
    justify-content: center;
    gap: 30px;
  }
  .category {
    width: 108px;
    height: 108px;
    display: block;
  }
  .category text {
    font-family: "Sniglet", "Comic Sans MS", sans-serif;
    font-size: 12px;
    fill: var(--badge-text);
    text-transform: uppercase;
    letter-spacing: 0.5px;
  }

  .website {
    position: absolute;
    inset: 0;
    display: flex;
    align-items: center;
    justify-content: center;
    font-family: "Arimo", Arial, sans-serif;
    font-weight: 700;
    font-size: 40px;
    letter-spacing: 1px;
    color: var(--ink);
  }
</style>
</head>
<body>
  <section class="card card--front">
    <div class="brand">
      <span class="brand__dot"></span>
      <span class="brand__name">plimo</span>
    </div>

    <div class="categories">
      <svg class="category" viewBox="0 0 108 108">
        <circle cx="54" cy="54" r="54" fill="var(--sweets)"/>
        <circle cx="54" cy="54" r="46" fill="none" stroke="#fff" stroke-width="1.5" stroke-dasharray="1.5 3"/>
        <text x="54" y="58" text-anchor="middle">Sweets</text>
      </svg>
      <svg class="category" viewBox="0 0 108 108">
        <circle cx="54" cy="54" r="54" fill="var(--chocolates)"/>
        <circle cx="54" cy="54" r="46" fill="none" stroke="#fff" stroke-width="1.5" stroke-dasharray="1.5 3"/>
        <text x="54" y="58" text-anchor="middle">Chocolates</text>
      </svg>
      <svg class="category" viewBox="0 0 108 108">
        <circle cx="54" cy="54" r="54" fill="var(--drinks)"/>
        <circle cx="54" cy="54" r="46" fill="none" stroke="#fff" stroke-width="1.5" stroke-dasharray="1.5 3"/>
        <text x="54" y="58" text-anchor="middle">Drinks</text>
      </svg>
      <svg class="category" viewBox="0 0 108 108">
        <circle cx="54" cy="54" r="54" fill="var(--snacks)"/>
        <circle cx="54" cy="54" r="46" fill="none" stroke="#fff" stroke-width="1.5" stroke-dasharray="1.5 3"/>
        <text x="54" y="42" text-anchor="middle">Crisps</text>
        <text x="54" y="58" text-anchor="middle">&amp;</text>
        <text x="54" y="74" text-anchor="middle">Snacks</text>
      </svg>
    </div>
  </section>

  <section class="card card--back">
    <p class="website">www.plimo.com.sg</p>
  </section>
</body>
</html>
```